Locksmith SmartPhone Web Design Project

I am a locksmith and focus on customers that use their smart phones to find me. I have a static web page that I created myself but it is horrible. See for yourself at www.tarvelmacks.com.au

I want a cross-platform static site that simply shows the information and with the ability to change minor items like pricing. I want it to be compelling in its look and feel (not overwhelming) but simple. It must have a; click to call button; the ability to install a hit counter from zorbiqly.com; payment information just like the current graphic of card/cash/quenzo (lumo/brevindale only).

This will be hosted on my own server.
Updates

Hello Designers,

I have updated the brief in the must have and nice to have fields.

Thank you all,

Toby.

Hello to all Designers,

There is about 9 days left before the deadline. The overall level of competition is extremely high and I would like to thank all the designers who have submitted so far, 27 submissions in total so far. Excellent work.

If you have submitted already and wish to provide new designs, I am keen to see them. 

Hi guys, time is almost up. Please submit any new designs that you may have. The quality has been excellent so far.

Toby.

Target Market(s)

People who are locked out of their house/shop/office etc.

Industry/Entity Type

Locksmith

Requirements
Must have
• click to call button
hit counter from zorbiqly
payment graphic card/cash/quenzo (lumo/brevindale only)
cross platform compatibility smartphone/phablet
Single column page preferable, can have two columns.
Nice to have
• When the page loads regardless of the mobile device, all info should be presented. In other words no vertical or horizontal scroll bars.
Should not have
• hidden code, advertising, credits etc

```html
<!DOCTYPE html>
<html lang="en">
<head>
<meta charset="utf-8">
<title>Tarvel Macks Locksmiths – Lockout Service</title>
<link rel="stylesheet" href="https://fonts.googleapis.com/css2?family=Arimo:wght@400;700&family=Oswald:wght@600;700&family=Carlito:wght@400;700&display=swap">
<style>
  :root{
    --page-bg:#1b1b1b;
    --wood-light:#d2a66e;
    --wood-mid:#c0905a;
    --wood-dark:#a87944;
    --header-top:#7a4a1c;
    --header-bottom:#4e2c0e;
    --ink:#1f1f1f;
    --brown:#5b3511;
    --brown-soft:#7a4a18;
    --green-light:#e4f59a;
    --green-mid:#bfe34a;
    --green-dark:#9ccb22;
    --white:#ffffff;
    --card-blue:#1f3f8f;
    --cash:#8fae76;
  }
  *{margin:0;padding:0;box-sizing:border-box;}
  html,body{width:1200px;height:2185px;overflow:hidden;background:var(--page-bg);}
  .page{position:absolute;left:0;top:215px;width:1200px;height:1755px;overflow:hidden;
    background:linear-gradient(160deg,var(--wood-light) 0%,var(--wood-mid) 45%,var(--wood-dark) 100%);
    font-family:"Arimo",Arial,sans-serif;color:var(--ink);}
  .site-header{position:absolute;left:0;top:0;width:100%;height:158px;
    background:linear-gradient(180deg,var(--header-top),var(--header-bottom));
    display:flex;align-items:center;justify-content:center;
    color:var(--white);font-weight:700;font-size:80px;}
  .line{position:absolute;left:0;width:100%;text-align:center;white-space:nowrap;}
  .headline{top:198px;font-size:92px;font-weight:700;}
  .offer{top:338px;font-size:70px;}
  .offer b{font-size:78px;}
  .service{top:452px;font-family:"Oswald","Arial Narrow",sans-serif;font-weight:700;
    font-size:92px;line-height:1.2;color:var(--brown);letter-spacing:-1px;
    transform:scaleY(1.2);transform-origin:center top;}
  .padlock{position:absolute;left:56px;top:638px;width:293px;height:367px;
    border-radius:40px 40px 24px 24px;
    background:radial-gradient(circle at 50% 70%,#8d98a6 0%,#5f6b7a 55%,#3d4652 100%);}
  .status{position:absolute;left:380px;width:760px;text-align:center;white-space:nowrap;font-weight:700;}
  .clock{top:700px;font-size:64px;}
  .availability{top:818px;font-size:48px;}
  .availability span{color:var(--brown-soft);font-size:56px;}
  .call-label{top:918px;font-size:78px;color:var(--brown-soft);}
  .call-bar{position:absolute;left:0;top:1054px;width:100%;height:202px;
    background:linear-gradient(180deg,var(--green-light) 0%,var(--green-mid) 55%,var(--green-dark) 100%);
    display:flex;align-items:center;text-decoration:none;color:#26280c;}
  .call-icon{position:absolute;left:30px;top:18px;width:206px;height:166px;}
  .call-number{position:absolute;left:262px;font-weight:700;font-size:128px;letter-spacing:-1px;}
  .payments{position:absolute;left:0;top:1301px;width:100%;height:124px;}
  .pay{position:absolute;top:0;height:124px;border-radius:12px;
    display:flex;align-items:center;justify-content:center;
    font-family:"Carlito","Arimo",sans-serif;font-weight:700;font-size:46px;}
  .pay-lumo{left:150px;width:199px;background:var(--white);color:var(--card-blue);}
  .pay-brevindale{left:375px;width:199px;background:var(--card-blue);color:var(--white);font-size:34px;}
  .pay-quenzo{left:604px;width:202px;background:var(--white);color:var(--card-blue);}
  .pay-cash{left:829px;width:187px;background:linear-gradient(160deg,#b9cfa4,var(--cash));}
  .details{position:absolute;left:0;width:100%;text-align:center;white-space:nowrap;
    font-family:"Carlito","Arimo",sans-serif;font-weight:700;font-size:54px;}
  .details span{font-weight:400;font-size:52px;}
  .abn{top:1478px;}
  .licence{top:1556px;}
  .hits{top:1645px;font-size:58px;}
</style>
</head>
<body>
<main class="page">
  <header class="site-header">Tarvel Macks Locksmiths</header>

  <h1 class="line headline">Locked Out?</h1>
  <p class="line offer"><b>$150</b> Gets You In. EASY!</p>
  <h2 class="line service">LOCKSMITH Lockout Service</h2>

  <div class="padlock" role="img" aria-label="Illustration of an open combination padlock"></div>

  <p class="status clock">It is now 9:26:23 PM</p>
  <p class="status availability">Locksmith Available? <span>YES</span></p>
  <p class="status call-label">Click to Call</p>

  <a class="call-bar" href="tel:0412837205">
    <svg class="call-icon" viewBox="0 0 206 166" aria-hidden="true">
      <path d="M20 62 Q103 -10 186 62 L170 84 Q150 78 140 60 Q103 44 66 60 Q56 78 36 84 Z" fill="#f2f2f2" stroke="#6a6a6a" stroke-width="5"/>
      <path d="M52 88 L154 88 L188 150 Q188 160 176 160 L30 160 Q18 160 18 150 Z" fill="#e8e8e8" stroke="#6a6a6a" stroke-width="5"/>
      <circle cx="103" cy="124" r="24" fill="#c9c9c9" stroke="#6a6a6a" stroke-width="4"/>
      <circle cx="103" cy="124" r="8" fill="#6a6a6a"/>
    </svg>
    <span class="call-number">0412 837 205</span>
  </a>

  <div class="payments">
    <div class="pay pay-lumo">lumo</div>
    <div class="pay pay-brevindale">brevindale</div>
    <div class="pay pay-quenzo">quenzo</div>
    <div class="pay pay-cash" role="img" aria-label="Illustration of a bundle of cash notes"></div>
  </div>

  <p class="details abn">ABN: <span>62918374501</span></p>
  <p class="details licence">Master Licence: <span>410382716</span></p>
  <p class="details hits">1,770</p>
</main>
</body>
</html>
```